IT Consulting Business Card Design

We need a business card on our company name....which is a IT consulting and staffing company. We also train masters graduates in various IT courses. 70% of the time these cards will be handed out to the graduate students at the universities. 30% for our clients and business partners. We are uploading our company logo...would like to see something that matches our logo or blends with it. Please visit www.brightvaleworks.com for more details on logo and colors.

Target Market(s)

70% of the time these cards will be handed out to the graduate students at the universities. 30% for our clients and business partners.

Industry/Entity Type

Business

Contact Information for Business Card

Ravi Kondamuri
Vice-President
Bright Vale Works Inc
3807 Morrow Lane, Suite 412
East Brookridge, NJ 07315
ravi@brightvaleworks.com
Office : 1-866-219-3840 X 515
Cell number : 732-581-9034

Requirements
Nice to have
• may be company logo and name on the back of the card and detials on the other side...just a thought..!!

```html
<!DOCTYPE html>
<html lang="en">
<head>
<meta charset="utf-8">
<title>Bright Vale Works – Business Card</title>
<link rel="stylesheet" href="https://fonts.googleapis.com/css2?family=Open+Sans:wght@400;600;700&display=swap">
<style>
  :root {
    --stage: #5e4a35;
    --card-dark: #1c1c1c;
    --card-dark-top: #3a3a3a;
    --card-light: #ffffff;
    --brand-red: #e01f26;
    --ink-grey: #555555;
    --ink-dark: #333333;
    --white: #ffffff;
  }
  * { box-sizing: border-box; margin: 0; padding: 0; }
  html, body {
    width: 1200px; height: 1000px; overflow: hidden;
    background: var(--stage);
    font-family: "Open Sans", Arial, sans-serif;
  }
  .canvas { position: relative; width: 1200px; height: 1000px; }

  /* Front: dark card */
  .card-front {
    position: absolute; left: 170px; top: 100px;
    width: 620px; height: 354px;
    background: radial-gradient(ellipse at 50% 30%, var(--card-dark-top), var(--card-dark) 70%);
    box-shadow: 0 10px 30px rgba(0,0,0,.45);
    display: flex; flex-direction: column; align-items: center; justify-content: center;
    gap: 18px;
  }
  .brand-mark {
    width: 130px; height: 130px; border-radius: 50%;
    background: var(--brand-red);
  }
  .brand-name {
    font-weight: 700; font-size: 40px; letter-spacing: .5px;
    color: var(--white); text-transform: uppercase;
  }
  .brand-url { font-size: 17px; color: var(--white); margin-top: -8px; }

  /* Back: white card */
  .card-back {
    position: absolute; left: 300px; top: 476px;
    width: 740px; height: 400px;
    background: var(--card-light);
    box-shadow: 0 10px 30px rgba(0,0,0,.45);
  }
  .holder { position: absolute; left: 62px; top: 120px; }
  .holder-name { font-weight: 700; font-size: 27px; color: var(--brand-red); margin-left: 18px; }
  .holder-title { font-size: 14.5px; color: var(--ink-grey); margin-top: 2px; }

  .back-brand {
    position: absolute; right: 44px; top: 42px;
    display: flex; flex-direction: column; align-items: center; gap: 10px;
  }
  .back-brand .brand-mark { width: 110px; height: 110px; }
  .back-brand .brand-label { font-weight: 700; font-size: 15px; color: var(--brand-red); text-transform: uppercase; }

  .contact-list {
    position: absolute; right: 28px; top: 248px;
    list-style: none; text-align: right;
  }
  .contact-list li {
    display: flex; align-items: center; justify-content: flex-end; gap: 8px;
    font-size: 15px; color: var(--ink-dark); line-height: 23px;
  }
  .contact-icon { width: 17px; height: 17px; flex: none; }

  .address-band {
    position: absolute; left: 0; right: 0; bottom: 0; height: 42px;
    background: var(--brand-red); color: var(--white);
    font-size: 15px; display: flex; align-items: center; justify-content: flex-end;
    padding-right: 26px;
  }
</style>
</head>
<body>
<main class="canvas">
  <section class="card-front" aria-label="Card front">
    <div class="brand-mark" aria-hidden="true"></div>
    <div class="brand-name">Bright Vale Works</div>
    <div class="brand-url">www.brightvaleworks.com</div>
  </section>

  <section class="card-back" aria-label="Card back">
    <div class="holder">
      <h1 class="holder-name">Ravi Kondamuri</h1>
      <p class="holder-title">Vice-President Bright Vale Works Inc</p>
    </div>

    <div class="back-brand">
      <div class="brand-mark" aria-hidden="true"></div>
      <div class="brand-label">Bright Vale Works</div>
    </div>

    <ul class="contact-list">
      <li>732-581-9034
        <svg class="contact-icon" viewBox="0 0 20 20" aria-hidden="true">
          <circle cx="10" cy="10" r="10" fill="var(--brand-red)"/>
          <rect x="7" y="4" width="6" height="12" rx="1.2" fill="none" stroke="#fff" stroke-width="1.5"/>
        </svg>
      </li>
      <li>1-866-219-3840 X 515
        <svg class="contact-icon" viewBox="0 0 20 20" aria-hidden="true">
          <circle cx="10" cy="10" r="10" fill="var(--brand-red)"/>
          <path d="M4.5 8.5 Q10 4 15.5 8.5 L14 10 L12 9 L12 7.8 Q10 7 8 7.8 L8 9 L6 10 Z" fill="#fff"/>
          <rect x="6" y="11" width="8" height="4" rx="1" fill="#fff"/>
        </svg>
      </li>
      <li>ravi@brightvaleworks.com
        <svg class="contact-icon" viewBox="0 0 20 20" aria-hidden="true">
          <circle cx="10" cy="10" r="10" fill="var(--brand-red)"/>
          <rect x="5" y="6.5" width="10" height="7" fill="#fff"/>
          <path d="M5 6.5 L10 11 L15 6.5" fill="none" stroke="var(--brand-red)" stroke-width="1.2"/>
        </svg>
      </li>
    </ul>

    <div class="address-band">3807 Morrow Lane, Suite 412 East Brookridge, NJ 07315</div>
  </section>
</main>
</body>
</html>
```